4th Generation Family Business Needs a New Card Design!

We are a family owned 4th Generation company. We are based in the Sydney, Australia area and we are desperately in need of a more modern and classy card. We are monumental masons who design, supply & erect lasting memorials throughout cemeteries in Sydney. Our customers are normally in a period of grieving. I have attached logo files that will need to be implemented on the card. Company was established 1935. Australian Owned and Operated. Card needs to be designed to PRINTLY.com specification.

Target Market(s)

Our target market is based upon people that a grieving for family members that have passed away. We also deal with alot of companies that own and operate cemeteries.

Industry/Entity Type

Business

Contact Information for Business Card

Gavin Pelham, Operations Manager, 0491726053, gavin@pelhamstoneworks.com.au
Brian Pelham, Director, 0417639285, brian@pelhamstoneworks.com.au
Phone # 02 9563 4820
Website: www.pelhamstoneworks.com.au
Address: Suite 17, 9 Lambert Lane, Kellyville, Sydney NSW 2155

Font styles to use
Serif
Decorative
Script

Requirements
Must have
• Would like to see the logo nicely implemented with a modern design. Embossed lettering would be a nice additive.

```html
<!DOCTYPE html>
<html lang="en">
<head>
<meta charset="utf-8">
<title>Pelham Stoneworks – Business Card</title>
<link href="https://fonts.googleapis.com/css2?family=Arimo:wght@400&display=swap" rel="stylesheet">
<style>
  :root {
    --canvas: #e9e6e1;
    --card: #ffffff;
    --ink: #2b2b2b;
    --ink-soft: #555555;
    --gold: #e9c531;
    --faint: #eeeeee;
  }
  * { margin: 0; padding: 0; box-sizing: border-box; }
  html, body { width: 1200px; height: 858px; overflow: hidden; }
  body {
    background: var(--canvas);
    font-family: "Arimo", Arial, sans-serif;
    color: var(--ink);
    display: flex;
    flex-direction: column;
    align-items: center;
    justify-content: center;
    gap: 40px;
  }
  .card {
    width: 640px;
    height: 366px;
    background: var(--card);
    position: relative;
    box-shadow: 0 6px 18px rgba(0,0,0,.12);
    overflow: hidden;
  }

  /* Front */
  .brand {
    position: absolute;
    display: flex;
    align-items: center;
    gap: 10px;
  }
  .brand-mark { width: 14px; height: 14px; background: var(--gold); flex: none; }
  .brand-name {
    font-size: 22px;
    letter-spacing: 3px;
    color: var(--ink);
    text-transform: uppercase;
    line-height: 1.15;
  }
  .front .brand { left: 38px; top: 160px; }
  .divider {
    position: absolute;
    left: 282px; top: 40px;
    width: 2px; height: 286px;
    background: var(--gold);
  }
  .people {
    position: absolute;
    left: 312px; top: 48px;
    display: flex;
    align-items: flex-start;
    gap: 12px;
  }
  .person-name { font-size: 19px; color: var(--ink); }
  .person-role { font-size: 13px; color: var(--ink-soft); margin-top: 3px; }
  .people .sep { width: 1.5px; height: 40px; background: var(--ink); }
  .contacts {
    position: absolute;
    left: 312px; top: 150px;
    list-style: none;
    font-size: 13.5px;
    line-height: 1.5;
    color: var(--ink);
  }
  .contacts li { display: flex; align-items: flex-start; gap: 10px; }
  .icon {
    width: 16px; height: 16px;
    background: var(--gold);
    border-radius: 2px;
    flex: none;
    margin-top: 2px;
    display: flex; align-items: center; justify-content: center;
  }
  .icon svg { width: 10px; height: 10px; }
  .icon.blank { background: transparent; }

  /* Back */
  .back-watermark {
    position: absolute;
    left: 0; right: 0; top: 110px;
    text-align: center;
    font-size: 54px;
    letter-spacing: 8px;
    color: var(--faint);
    text-transform: uppercase;
  }
  .back .brand { right: 36px; bottom: 34px; }
  .back .brand-name { font-size: 15px; letter-spacing: 2px; }
  .back .brand-mark { width: 10px; height: 10px; }
</style>
</head>
<body>

<section class="card front" aria-label="Card front">
  <div class="brand">
    <span class="brand-mark"></span>
    <span class="brand-name">Pelham<br>Stoneworks</span>
  </div>
  <div class="divider"></div>

  <div class="people">
    <div class="person">
      <div class="person-name">Gavin Pelham</div>
      <div class="person-role">Operations Manager</div>
    </div>
    <span class="sep"></span>
    <div class="person">
      <div class="person-name">Brian Pelham</div>
      <div class="person-role">Director</div>
    </div>
  </div>

  <ul class="contacts">
    <li><span class="icon"><svg viewBox="0 0 10 10"><rect x="3" y="1" width="4" height="8" rx="0.8" fill="none" stroke="#fff" stroke-width="1"/></svg></span>0491726053 / 0417639285</li>
    <li><span class="icon"><svg viewBox="0 0 10 10"><path d="M2 1.5l2 .3.6 2-1 .9a5 5 0 0 0 1.7 1.7l.9-1 2 .6.3 2C6 9 1 4 2 1.5z" fill="#fff"/></svg></span>02 9563 4820</li>
    <li><span class="icon"><svg viewBox="0 0 10 10"><rect x="1" y="2.5" width="8" height="5" fill="none" stroke="#fff" stroke-width="1"/><path d="M1 2.5l4 3 4-3" fill="none" stroke="#fff" stroke-width="1"/></svg></span>gavin@pelhamstoneworks.com.au</li>
    <li><span class="icon blank"></span>brian@pelhamstoneworks.com.au</li>
    <li><span class="icon"><svg viewBox="0 0 10 10"><circle cx="5" cy="5" r="3.8" fill="none" stroke="#fff" stroke-width="1"/><path d="M1.2 5h7.6M5 1.2c-2 2.5-2 5 0 7.6M5 1.2c2 2.5 2 5 0 7.6" fill="none" stroke="#fff" stroke-width=".8"/></svg></span>www.pelhamstoneworks.com.au</li>
    <li><span class="icon"><svg viewBox="0 0 10 10"><path d="M5 9.5S1.8 6 1.8 4a3.2 3.2 0 0 1 6.4 0C8.2 6 5 9.5 5 9.5z" fill="#fff"/><circle cx="5" cy="4" r="1.1" fill="#e9c531"/></svg></span>Suite 17, 9 Lambert Lane, Kellyville,<br>Sydney NSW 2155</li>
  </ul>
</section>

<section class="card back" aria-label="Card back">
  <div class="back-watermark" aria-hidden="true">Pelham</div>
  <div class="brand">
    <span class="brand-mark"></span>
    <span class="brand-name">Pelham Stoneworks</span>
  </div>
</section>

</body>
</html>
```